Bright Towns Alliance PowerPoint Design Template and Sample Deck

The Bright Towns Alliance is an international organization that seeks to improve the livability, workability and sustainability of the world’s cities.
We seek a versatile PowerPoint design template with 10 slide types plus a “self-documenting” sample deck. Your design will be used in keynote speeches and workshops around the world.
After the contest is completed, we will ask the winning designer to add 10-20 additional slide types for $75 per slide. We also seek a long-term relationship whereby we can request “custom” slides and/or ask the designer to touch up the slides we build to make them better.
FILES. We have uploaded several files:
2. PALETTE. Shows our official colors.
3 LOGOS. Several individual files with different variations of our logo. Some with our motto, some without.
2. SAMPLE SLIDES. Because we were unable to successfully upload our sample deck, we are making it available via this FileCrate link:
https://www.filecrate-example.net/s/q7mrk2tzw9hdn4e/The%20Bright%20Towns%20Alliance%20Design%20Contest%20Notes.docx?dl=0
Target Market(s)
Mayors, department heads, CIOs, senior executives from technology companies
Industry/Entity Type
Information Technology
Colors
Designer to choose colors to be used in the design.
Requirements
Must have
- Please see uploaded Word document for requirements, nice to haves and should not haves and uploaded palette for color preferences.
Nice to have
- see above
Should not have
- see above

```html
<!DOCTYPE html>
<html lang="en">
<head>
<meta charset="utf-8">
<title>Bright Towns Alliance – Slide Template</title>
<link rel="stylesheet" href="https://fonts.googleapis.com/css2?family=Montserrat:wght@400;500;700&display=swap">
<style>
  :root {
    --backdrop: #a9a9ab;
    --white: #ffffff;
    --navy: #1e1f5c;
    --navy-deep: #141a4a;
    --blue: #1d6fc2;
    --sky: #3fa3e0;
    --orange: #f38a1f;
    --ink: #111111;
    --grey-dark: #2b2f33;
    --grey-mid: #6e7478;
    --teal-dark: #23474d;
  }
  * { box-sizing: border-box; margin: 0; padding: 0; }
  html, body { width: 1200px; height: 900px; overflow: hidden; }
  body {
    background: var(--backdrop);
    font-family: "Montserrat", sans-serif;
    position: relative;
  }
  .slide {
    position: absolute;
    width: 517px;
    height: 399px;
    background: var(--white);
    overflow: hidden;
    box-shadow: 0 2px 8px rgba(0,0,0,.25);
  }
  .slide--agenda { left: 84px; top: 41px; }
  .slide--title  { left: 626px; top: 41px; }
  .slide--quote  { left: 84px; top: 459px; }
  .slide--text   { left: 620px; top: 459px; }

  .accent-band {
    position: absolute; left: 0; bottom: 0;
    width: 100%; height: 16px;
    background: var(--orange);
  }
  .photo { position: absolute; display: block; }

  .brand-name {
    position: absolute;
    font-weight: 400;
    color: var(--navy);
    font-size: 19px;
    line-height: 20px;
    letter-spacing: -0.3px;
  }

  /* Agenda slide */
  .agenda-title {
    position: absolute; left: 30px; top: 46px;
    color: var(--white);
    font-size: 30px; line-height: 37px; font-weight: 400;
  }
  .agenda-title strong { font-weight: 700; }
  .agenda-list {
    position: absolute; left: 208px; top: 140px;
    list-style: none; width: 272px;
  }
  .agenda-list li {
    display: flex; align-items: baseline;
    font-size: 11.5px; line-height: 20.8px; color: var(--ink);
    position: relative; padding-left: 12px;
  }
  .agenda-list li::before {
    content: ""; position: absolute; left: 0; top: 8px;
    width: 5px; height: 5px; border-radius: 50%;
    background: var(--orange);
  }
  .agenda-list b { font-weight: 700; margin-right: 4px; }
  .agenda-list .leader {
    flex: 1; border-bottom: 1px dotted var(--ink);
    margin: 0 4px; transform: translateY(-3px);
  }

  /* Title slide */
  .cover-title {
    position: absolute; left: 22px; top: 112px;
    color: var(--white);
    font-size: 48px; line-height: 52px; font-weight: 400;
  }
  .cover-title strong { font-weight: 700; }
  .cover-subtitle {
    position: absolute; left: 23px; top: 165px;
    color: var(--white); font-size: 17px; font-weight: 400;
  }

  /* Quote slide */
  .quote-block {
    position: absolute; left: 316px; top: 66px; width: 166px;
    border-top: 1px solid rgba(255,255,255,.7);
    border-bottom: 1px solid rgba(255,255,255,.7);
    padding: 6px 0 7px;
    color: var(--white);
    font-size: 11.5px; line-height: 14px; text-align: center;
  }
  .brand-tile {
    position: absolute; left: 426px; top: 315px;
    width: 74px; height: 64px; background: var(--white);
  }
  .brand-tile .brand-name {
    left: 2px; top: 2px; font-size: 16px; line-height: 20px;
  }

  /* Text slide */
  .section-heading {
    position: absolute; left: 202px; top: 84px;
    font-size: 21px; font-weight: 400; color: var(--navy);
  }
  .section-heading strong { font-weight: 700; }
  .body-copy {
    position: absolute; left: 197px; top: 122px; width: 290px;
    font-size: 11.6px; line-height: 14.1px; color: var(--navy);
  }
  .point-list {
    position: absolute; left: 203px; top: 277px;
    list-style: none; font-size: 11.6px; line-height: 14.1px; color: var(--navy);
  }
  .point-list li { position: relative; padding-left: 8px; }
  .point-list li::before {
    content: ""; position: absolute; left: 0; top: 5px;
    width: 5px; height: 5px; border-radius: 50%; background: var(--orange);
  }
</style>
</head>
<body>

<!-- Agenda slide -->
<section class="slide slide--agenda">
  <svg class="photo" width="517" height="399" viewBox="0 0 517 399" role="img" aria-label="Night city photo with glass towers and red light trails, cut on a diagonal">
    <defs>
      <linearGradient id="agendaPhoto" x1="0" y1="0" x2="0.4" y2="1">
        <stop offset="0" stop-color="#1b1f62"/>
        <stop offset="0.45" stop-color="#1d4f96"/>
        <stop offset="0.75" stop-color="#2a3d6a"/>
        <stop offset="0.88" stop-color="#a4304a"/>
        <stop offset="1" stop-color="#2a2f45"/>
      </linearGradient>
    </defs>
    <polygon points="0,0 288,0 112,383 0,383" fill="url(#agendaPhoto)"/>
    <polygon points="0,0 288,0 233,129 0,129" fill="#1e1f5c" opacity="0.55"/>
  </svg>
  <h1 class="agenda-title">Progressive<br><strong>Agenda</strong></h1>
  <div class="brand-name" style="left:423px; top:16px;">Bright<br>Towns<br>Alliance</div>
  <ul class="agenda-list">
    <li><b>Lorem Ipsum</b> dolor sit amet<span class="leader"></span>01</li>
    <li><b>Lorem Ipsum</b> dolor sit amet<span class="leader"></span>01</li>
    <li><b>Lorem Ipsum</b> dolor sit amet<span class="leader"></span>01</li>
    <li><b>Lorem Ipsum</b> dolor sit amet<span class="leader"></span>01</li>
    <li><b>Lorem Ipsum</b> dolor sit amet<span class="leader"></span>01</li>
    <li><b>Lorem Ipsum</b> dolor sit amet<span class="leader"></span>01</li>
  </ul>
  <div class="accent-band"></div>
</section>

<!-- Title slide -->
<section class="slide slide--title">
  <svg class="photo" width="517" height="383" viewBox="0 0 517 383" role="img" aria-label="Daytime city skyline strip above a night city scene with towers and light trails">
    <defs>
      <linearGradient id="skyline" x1="0" y1="0" x2="0" y2="1">
        <stop offset="0" stop-color="#9fb8d0"/>
        <stop offset="0.6" stop-color="#7d8c98"/>
        <stop offset="1" stop-color="#5b6a60"/>
      </linearGradient>
      <linearGradient id="nightCity" x1="0" y1="0" x2="0.3" y2="1">
        <stop offset="0" stop-color="#1e1f5c"/>
        <stop offset="0.5" stop-color="#1f5fa8"/>
        <stop offset="0.85" stop-color="#3a3f8a"/>
        <stop offset="1" stop-color="#b0394f"/>
      </linearGradient>
    </defs>
    <rect x="0" y="0" width="517" height="106" fill="url(#skyline)"/>
    <rect x="0" y="106" width="517" height="277" fill="url(#nightCity)"/>
  </svg>
  <h1 class="cover-title">Your <strong>Title</strong></h1>
  <p class="cover-subtitle">Lorem ipsum dolor sit amet</p>
  <div class="accent-band"></div>
</section>

<!-- Quote slide -->
<section class="slide slide--quote">
  <svg class="photo" width="517" height="383" viewBox="0 0 517 383" role="img" aria-label="Black and white portrait of a smiling man with glasses, hands pressed together, over a dark teal faceted backdrop">
    <defs>
      <linearGradient id="portrait" x1="0" y1="0" x2="1" y2="0">
        <stop offset="0" stop-color="#8a8d8f"/>
        <stop offset="0.45" stop-color="#4a4f52"/>
        <stop offset="0.7" stop-color="#2c4a50"/>
        <stop offset="1" stop-color="#2f5e64"/>
      </linearGradient>
    </defs>
    <rect width="517" height="383" fill="url(#portrait)"/>
  </svg>
  <blockquote class="quote-block">Lorem ipsum dolor sit amet, consectetur adipiscing elit, sed do eiusmod tempor incididunt ut labore et dolore magna aliqua. Ut enim ad minim veniam, quis nostrud exercitation ullamco laboris nisi ut aliquip ex ea commodo consequat.</blockquote>
  <div class="brand-tile"><div class="brand-name">Bright<br>Towns<br>Alliance</div></div>
  <div class="accent-band"></div>
</section>

<!-- Text slide -->
<section class="slide slide--text">
  <svg class="photo" width="517" height="383" viewBox="0 0 517 383" role="img" aria-label="Blue night city photo of glass towers and a lit street, cut on a diagonal">
    <defs>
      <linearGradient id="textPhoto" x1="0" y1="0" x2="0.3" y2="1">
        <stop offset="0" stop-color="#1e1f5c"/>
        <stop offset="0.5" stop-color="#1c6ab8"/>
        <stop offset="0.85" stop-color="#3da0dc"/>
        <stop offset="1" stop-color="#2a4f8a"/>
      </linearGradient>
    </defs>
    <polygon points="0,0 198,0 78,383 0,383" fill="url(#textPhoto)"/>
  </svg>
  <div class="brand-name" style="left:423px; top:18px;">Bright<br>Towns<br>Alliance</div>
  <h2 class="section-heading">Progressive<strong>Agenda</strong></h2>
  <p class="body-copy">"Lorem ipsum dolor sit amet, consectetur adipiscing elit, sed do eiusmod tempor incididunt ut labore et dolore magna aliqua. Ut enim ad minim veniam, quis nostrud exercitation ullamco laboris nisi ut aliquip ex ea commodo consequat. Duis aute irure dolor in reprehenderit in voluptate velit esse cillum dolore eu fugiat nulla pariatur. Excepteur sint occaecat cupidatat non proident, sunt in culpa qui officia deserunt mollit anim id est laborum."</p>
  <ul class="point-list">
    <li>Excepteur sint occaecat cupidatat</li>
    <li>Duis aute irure dolor in</li>
    <li>Ut enim ad minim veniam</li>
    <li>officia deserunt mollit anim</li>
  </ul>
  <div class="accent-band"></div>
</section>

</body>
</html>
```